Real Estate "For Sale" Sign for construction company

We need a sign that we can use to hang on a post and place on the road when we sell a property. The sign will be simple and will need to mainly feature our logo (files attached), as well as the words "For Sale", and then our phone number "(555) 617 3489". The sign will hang on a post that'll look something like the attached picture.

Target Market(s)

Home buyers

Industry/Entity Type

Real Estate

Font styles to use
Serif
Sans Serif

Colors
0054AA
0677BA
7BADD7
CADEEF
E8F1F8
0094D4
00A9DD
6FCCEA
C7EBF8
E9F6FB

Requirements
Must have
• For Sale & our phone number

```html
<!DOCTYPE html>
<html lang="en">
<head>
<meta charset="utf-8">
<title>For Sale Sign – Two Colourways</title>
<link href="https://fonts.googleapis.com/css2?family=Oswald:wght@400&display=swap" rel="stylesheet">
<style>
  :root {
    --paper: #ffffff;
    --edge: #b9bcc2;
    --navy: #131f4c;
    --sky: #1884c7;
    --brand: #0677ba;
    --phone: #0a4fa3;
    --text-light: #ffffff;
  }
  * { box-sizing: border-box; margin: 0; padding: 0; }
  html, body {
    width: 1200px;
    height: 400px;
    overflow: hidden;
    background: var(--paper);
  }
  .canvas {
    position: relative;
    width: 1200px;
    height: 400px;
    display: flex;
    justify-content: center;
    align-items: center;
    gap: 80px;
    font-family: "Oswald", "Arial Narrow", sans-serif;
  }
  .sign {
    position: relative;
    width: 270px;
    height: 358px;
    background: var(--paper);
    border: 1px solid var(--edge);
    display: flex;
    flex-direction: column;
  }
  .sign__brand {
    height: 132px;
    display: flex;
    align-items: center;
    justify-content: center;
    gap: 8px;
    padding-top: 14px;
  }
  .brand-dot {
    width: 18px;
    height: 18px;
    border-radius: 50%;
    background: var(--brand);
  }
  .brand-name {
    font-size: 24px;
    font-weight: 400;
    color: var(--brand);
    letter-spacing: 0.5px;
  }
  .sign__band {
    height: 116px;
    display: flex;
    align-items: center;
    justify-content: center;
    color: var(--text-light);
    font-size: 60px;
    font-weight: 400;
    letter-spacing: 1px;
  }
  .sign--navy .sign__band { background: var(--navy); }
  .sign--sky .sign__band { background: var(--sky); }
  .sign__phone {
    flex: 1;
    display: flex;
    align-items: center;
    justify-content: center;
    color: var(--phone);
    font-size: 38px;
    font-weight: 400;
    padding-bottom: 8px;
  }
</style>
</head>
<body>
  <main class="canvas">
    <section class="sign sign--navy">
      <div class="sign__brand">
        <span class="brand-dot"></span>
        <span class="brand-name">Hollow Pine Estates</span>
      </div>
      <div class="sign__band">FOR SALE</div>
      <div class="sign__phone">(555) 617 3489</div>
    </section>
    <section class="sign sign--sky">
      <div class="sign__brand">
        <span class="brand-dot"></span>
        <span class="brand-name">Hollow Pine Estates</span>
      </div>
      <div class="sign__band">FOR SALE</div>
      <div class="sign__phone">(555) 617 3489</div>
    </section>
  </main>
</body>
</html>
```